Darrow Consulting needs a quality & professional business card!

I am a recruitment and employment consultant from Brisbane, Australia and I had a fantastic logo organised by this community to I am hoping the business card will be the same.

I have attached the Darrow consulting logo that ideally would feature on the back of the business card. There are a number of logos for you to use as you see fit. I would like the colour cheme to match that of the Darrow Consulting logo. I also have a secondary company called Career Lantern Australia and I have included that logo as well. While it is an important part of the business I don't want this logo feature too predominantly as I am moving out of this space. This logo was created by myself and is of low quality. Feel free to use the icon and words however you want. The winning design will be smart, professional and eye-catching.

The information I am looking for in the business card is:
Name: Gavin Darrow
Position: Founder & Director
Phone: (07) 3519 6482
Mobile: 0431 586 207
Email: gavin@careerlantern.com.au

Target Market(s)

Recruiters, government, large companies

Contact Information for Business Card

Name: Gavin Darrow
Phone: (07) 3519 6482
Mobile: 0431 586 207
Web: www.careerlantern.com.au

Font styles to use
Serif
Sans Serif

Requirements
Must have
• Darrow Consulting Logo on reverse side
• Contact details on front side with smaller reference to Darrow Consulting logo and Career Lantern Australia logo

```html
<!DOCTYPE html>
<html lang="en">
<head>
<meta charset="utf-8">
<title>Darrow Consulting – Business Card</title>
<link href="https://fonts.googleapis.com/css2?family=Roboto:wght@400;500;700&family=Noto+Serif:wght@700&display=swap" rel="stylesheet">
<style>
  :root {
    --backdrop: #2e3135;
    --brand-blue: #1a9bcf;
    --panel-dark: #333333;
    --card-white: #ffffff;
    --ink: #1f1f1f;
    --ink-soft: #3a3a3a;
  }
  * { box-sizing: border-box; margin: 0; padding: 0; }
  html, body {
    width: 1200px; height: 1141px; overflow: hidden;
    background: var(--backdrop);
    font-family: "Roboto", Arial, sans-serif;
  }
  .card {
    position: absolute; left: 232px; width: 730px;
    background: var(--card-white);
    border-radius: 34px; overflow: hidden;
  }
  .card--front { top: 120px; height: 416px; }
  .card--back  { top: 570px; height: 412px; }

  /* Front: contact column */
  .contact-column { position: absolute; left: 0; top: 0; width: 319px; height: 100%; }
  .band { position: absolute; left: 0; width: 100%; color: #fff; }
  .band--name { top: 0; height: 116px; background: var(--brand-blue); padding: 37px 0 0 31px; }
  .band--details { top: 116px; height: 187px; background: var(--panel-dark); padding-top: 40px; }
  .band--company { top: 303px; height: 113px; background: var(--brand-blue); padding: 28px 0 0 31px; }
  .person-name { font-weight: 700; font-size: 24px; letter-spacing: 0.2px; }
  .person-role { font-size: 16px; margin-top: 4px; }
  .contact-list { list-style: none; }
  .contact-item {
    display: flex; align-items: center; height: 25.7px;
    padding-left: 35px; font-size: 16px; color: #f2f2f2;
  }
  .contact-icon { width: 16px; height: 16px; margin-right: 14px; fill: var(--brand-blue); flex: none; }
  .company-name { font-weight: 500; font-size: 26px; }
  .company-region { font-size: 16px; margin-top: 3px; }

  /* Front: brand side */
  .brand-side {
    position: absolute; left: 319px; top: 0; width: 411px; height: 100%;
    display: flex; flex-direction: column; align-items: center;
  }
  .brand-dot {
    width: 88px; height: 88px; border-radius: 50%;
    background: var(--ink); margin-top: 100px;
  }
  .firm-name {
    font-family: "Roboto", Arial, sans-serif; font-weight: 500;
    color: var(--ink-soft); letter-spacing: 1px; text-transform: uppercase;
  }
  .brand-side .firm-name { font-size: 30px; margin-top: 50px; }

  /* Back */
  .back-heading { position: absolute; left: 159px; top: 38px; color: var(--ink); }
  .back-title { font-family: "Noto Serif", Georgia, serif; font-weight: 700; font-size: 56px; line-height: 1; }
  .back-region { font-size: 30px; color: var(--ink-soft); margin-top: 10px; }
  .back-brand { position: absolute; left: 0; width: 100%; top: 240px; text-align: center; }
  .back-brand .firm-name { font-size: 40px; }
  .back-web {
    position: absolute; left: 0; width: 100%; top: 350px;
    text-align: center; font-size: 17px; color: var(--ink);
  }
</style>
</head>
<body>
  <section class="card card--front">
    <div class="contact-column">
      <div class="band band--name">
        <div class="person-name">GAVIN DARROW</div>
        <div class="person-role">Founder &amp; Director</div>
      </div>
      <div class="band band--details">
        <ul class="contact-list">
          <li class="contact-item">
            <svg class="contact-icon" viewBox="0 0 16 16" aria-hidden="true"><path d="M1 5c0-2 3-3 7-3s7 1 7 3v1h-4V4.5H5V6H1z"/><path d="M3 8l2-2h6l2 2v6H3z M8 9a2 2 0 1 0 0.01 0z"/></svg>
            (07) 3519 6482
          </li>
          <li class="contact-item">
            <svg class="contact-icon" viewBox="0 0 16 16" aria-hidden="true"><path d="M3 1l3 3-1.5 2c1 2 3 4 5 5l2-1.5 3 3-2 2C7 14 2 9 1 3z"/></svg>
            0431 586 207
          </li>
          <li class="contact-item">
            <svg class="contact-icon" viewBox="0 0 16 16" aria-hidden="true"><path d="M1 3h14v1.5L8 9 1 4.5z M1 6l7 4.5L15 6v7H1z"/></svg>
            gavin@careerlantern.com.au
          </li>
          <li class="contact-item">
            <svg class="contact-icon" viewBox="0 0 16 16" aria-hidden="true"><circle cx="8" cy="8" r="7"/><path d="M8 1v14M1 8h14M3 4h10M3 12h10" stroke="#333" stroke-width="1" fill="none"/></svg>
            www.careerlantern.com.au
          </li>
        </ul>
      </div>
      <div class="band band--company">
        <div class="company-name">Career Lantern</div>
        <div class="company-region">Australia</div>
      </div>
    </div>
    <div class="brand-side">
      <div class="brand-dot"></div>
      <div class="firm-name">Darrow Consulting</div>
    </div>
  </section>

  <section class="card card--back">
    <div class="back-heading">
      <div class="back-title">Career Lantern</div>
      <div class="back-region">Australia</div>
    </div>
    <div class="back-brand">
      <div class="firm-name">Darrow Consulting</div>
    </div>
    <div class="back-web">www.careerlantern.com.au</div>
  </section>
</body>
</html>
```